Letterhead Design Needed for Real Estate Office

We are a boutique real estate agency focused on property management. We need a letter head which is professional looking and include the following information:

Logo
ABN Number
Address
Postal Address
Phone
Fax
Mobile
Email
Website

Please note that the PLVAQT logo can not be changed and must be positioned at the bottom right corner.

Please find attached the existing letterhead design for all the required elements.

Target Market(s)

Letterhead mostly used for service of notices, business letters, clients communication

Industry/Entity Type

Boutique

Colors

Designer to choose colors to be used in the design.

Requirements
Must have
• Logo

```html
<!DOCTYPE html>
<html lang="en">
<head>
<meta charset="utf-8">
<title>PLVAQT Letterhead</title>
<link rel="stylesheet" href="https://fonts.googleapis.com/css2?family=Lato:wght@700;900&display=swap">
<style>
  :root {
    --band-blue: #5ab4dc;
    --deep-blue: #0590c8;
    --ink: #1b1b1b;
    --paper: #ffffff;
    --brand-blue: #1d5fa8;
  }
  * { margin: 0; padding: 0; box-sizing: border-box; }
  html, body { width: 848px; height: 1200px; overflow: hidden; background: var(--paper); }
  .letterhead {
    position: relative;
    width: 848px;
    height: 1200px;
    background: var(--paper);
    font-family: "Lato", Arial, sans-serif;
    color: var(--ink);
    overflow: hidden;
  }
  .contact-band {
    position: absolute;
    left: 0; top: 0;
    width: 848px;
    height: 80px;
    background: var(--band-blue);
  }
  .contact-item {
    position: absolute;
    display: flex;
    align-items: center;
    font-size: 12.5px;
    font-weight: 700;
    white-space: nowrap;
    line-height: 1;
  }
  .contact-item svg { display: block; flex: none; fill: var(--ink); }
  .contact-item .label { margin-left: var(--gap, 12px); }
  .row-one { top: 14px; height: 24px; }
  .row-two { top: 49px; height: 24px; }

  .abn    { left: 49px;  --gap: 11px; }
  .street { left: 187px; --gap: 12px; }
  .postal { left: 608px; --gap: 9px; }
  .mobile { left: 98px;  --gap: 13px; }
  .phone  { left: 219px; --gap: 12px; }
  .fax    { left: 336px; --gap: 17px; }
  .email  { left: 466px; --gap: 15px; }
  .web    { left: 623px; --gap: 14px; }

  .footer-swoosh {
    position: absolute;
    left: 0; bottom: 0;
    width: 848px;
    height: 260px;
  }
  .swoosh-deep { fill: var(--deep-blue); }
  .swoosh-light { fill: var(--band-blue); }

  .brand-mark {
    position: absolute;
    left: 600px;
    top: 1080px;
    display: flex;
    align-items: center;
    gap: 12px;
  }
  .brand-square {
    width: 20px;
    height: 20px;
    background: var(--brand-blue);
  }
  .brand-name {
    font-family: "Lato", Arial, sans-serif;
    font-weight: 900;
    font-size: 44px;
    letter-spacing: -1px;
    color: var(--brand-blue);
    line-height: 1;
  }
</style>
</head>
<body>
<div class="letterhead">
  <header class="contact-band">
    <div class="contact-item row-one abn">
      <svg width="30" height="22" viewBox="0 0 30 22" aria-hidden="true">
        <rect x="1" y="2" width="28" height="18" rx="3"/>
        <rect x="5" y="7" width="9" height="2.5" fill="#5ab4dc"/>
        <rect x="5" y="12" width="14" height="2.5" fill="#5ab4dc"/>
      </svg>
      <span class="label">12 345 678 901</span>
    </div>
    <div class="contact-item row-one street">
      <svg width="17" height="24" viewBox="0 0 17 24" aria-hidden="true">
        <path d="M8.5 0C3.8 0 0 3.7 0 8.3 0 14.5 8.5 24 8.5 24S17 14.5 17 8.3C17 3.7 13.2 0 8.5 0Zm0 11.5a3.2 3.2 0 1 1 0-6.4 3.2 3.2 0 0 1 0 6.4Z"/>
      </svg>
      <span class="label">Shop 12B 210-218 Harbour Avenue Lindfield NSW 2070 Australia</span>
    </div>
    <div class="contact-item row-one postal">
      <svg width="35" height="24" viewBox="0 0 35 24" aria-hidden="true">
        <path d="M8 1h22a5 5 0 0 1 5 5v11H1V8a7 7 0 0 1 7-7Z"/>
        <rect x="5" y="6" width="5" height="7" fill="#5ab4dc"/>
        <rect x="14" y="7" width="14" height="2.5" fill="#5ab4dc"/>
        <rect x="16" y="17" width="4" height="7"/>
      </svg>
      <span class="label">415 Lindfield NSW 2070</span>
    </div>

    <div class="contact-item row-two mobile">
      <svg width="14" height="24" viewBox="0 0 14 24" aria-hidden="true">
        <path d="M2.5 0h9A2.5 2.5 0 0 1 14 2.5v19a2.5 2.5 0 0 1-2.5 2.5h-9A2.5 2.5 0 0 1 0 21.5v-19A2.5 2.5 0 0 1 2.5 0Zm-.5 3v16h10V3Z"/>
        <circle cx="7" cy="21.4" r="1.1" fill="#5ab4dc"/>
      </svg>
      <span class="label">0400 123 456</span>
    </div>
    <div class="contact-item row-two phone">
      <svg width="21" height="24" viewBox="0 0 21 24" aria-hidden="true">
        <path d="M4 1 8 0l3 6-3 2.5c1.2 3.8 3.3 7 6.5 9.5L17 15.5l4 4.5-2.5 3.5C9 23 1 12 4 1Z"/>
      </svg>
      <span class="label">9000 1234</span>
    </div>
    <div class="contact-item row-two fax">
      <svg width="26" height="24" viewBox="0 0 26 24" aria-hidden="true">
        <path d="M7 0h12v9h-2V2H9v7H7Z"/>
        <rect x="10.5" y="4" width="5" height="1.4"/>
        <rect x="10.5" y="6.5" width="5" height="1.4"/>
        <path d="M2 11h22a2 2 0 0 1 2 2v9a2 2 0 0 1-2 2H2a2 2 0 0 1-2-2v-9a2 2 0 0 1 2-2Zm3 4v3h16v-3Z"/>
      </svg>
      <span class="label">9000 5678</span>
    </div>
    <div class="contact-item row-two email">
      <svg width="38" height="24" viewBox="0 0 38 24" aria-hidden="true">
        <rect x="0" y="0" width="38" height="24"/>
        <path d="M1.5 1.5 19 14 36.5 1.5" fill="none" stroke="#5ab4dc" stroke-width="1.8"/>
        <path d="M1.5 22.5 14 10.5M36.5 22.5 24 10.5" fill="none" stroke="#5ab4dc" stroke-width="1.8"/>
      </svg>
      <span class="label">info@hlre.cc</span>
    </div>
    <div class="contact-item row-two web">
      <svg width="31" height="24" viewBox="0 0 31 24" aria-hidden="true">
        <path d="M0 0h31v24H0Zm2 6v16h27V6Z"/>
        <rect x="4" y="9" width="10" height="2"/>
        <rect x="4" y="13" width="10" height="2"/>
        <rect x="4" y="17" width="7" height="2"/>
        <rect x="18" y="11" width="4" height="4"/>
        <rect x="22" y="15" width="4" height="4"/>
      </svg>
      <span class="label">HTTP://hlre.cc</span>
    </div>
  </header>

  <svg class="footer-swoosh" viewBox="0 940 848 260" aria-hidden="true">
    <path class="swoosh-deep" d="M0 947 Q 190 1160 551 1200 L0 1200 Z"/>
    <path class="swoosh-light" d="M0 982 Q 110 1150 254 1200 L0 1200 Z"/>
  </svg>

  <div class="brand-mark">
    <span class="brand-square"></span>
    <span class="brand-name">PLVAQT</span>
  </div>
</div>
</body>
</html>
```